Yard Nest+ - Outdoors Home Improvents, Upkeeing and Maintenance services

I need a website that looks environmental and refreshing. Yard Nest+ is a home upkeeping services and maintenance for all seasons. I will need a website that can create the feel or atmosphere of each season in separate tabs (ie for summer design should illustrate lawn mowing and gardening services etc while the winter would illustrate snow shovelling services likewise for fall illustratating leaves raking services. Each service should have there own feel to it as if the pages/tab was solely dedicated to that service. Four services in total winter, fall, spring, summer and would like it to have a fun and engaging feel to it with rollover images and links to service description pages.
Updates

Sorry name of the company is maple ridge can you revise the name. I will add a picture to the brief you can get the logo from Added Thursday, April 14, 2016

Target Market(s)

Home Owners, rental suites, landlords, real estate commercial/residential

Industry/Entity Type

Home Improvement

Number of Pages Required

4 page

Font styles to use
Serif
Decorative
Script

Colors
33b8a4
add136
fbee3d
ffffff
ec1f27
ffc214
f37122
f78f20
1b1b1b

Requirements
Must have
• Each service should have there own feel to it as if the pages/tab was solely dedicated to that service. Four services in total winter, fall, spring, summer and would like it to have a fun and engaging feel to it with rollover images and links to service description pages.
Nice to have
Should not have
• Dull and unwelcoming

```html
<!DOCTYPE html>
<html lang="en">
<head>
<meta charset="utf-8">
<title>Maple Ridge – Home Upkeep for All Seasons</title>
<link href="https://fonts.googleapis.com/css2?family=Cinzel:wght@400;700&family=Lato:wght@400;700&display=swap" rel="stylesheet">
<style>
:root{
  --teal:#33b8a4;
  --teal-soft:#3dbda9;
  --ink:#1b1b1b;
  --text:#222;
  --grey:#6b6b6b;
  --line:#d6d6d6;
  --field:#f3f3f3;
  --orange:#f78f20;
  --white:#ffffff;
}
*{box-sizing:border-box;margin:0;padding:0}
html,body{width:982px;height:1200px;overflow:hidden;background:var(--white)}
body{position:relative;font-family:'Lato',sans-serif;color:var(--text)}
.abs{position:absolute}
.topbar{left:0;top:0;width:982px;height:3px;background:#2b2420}

/* header */
.brand{left:58px;top:0;width:192px;height:152px;background:var(--white);box-shadow:0 1px 4px rgba(0,0,0,.25);z-index:3;padding:5px}
.brand-inner{width:100%;height:100%;border:1px dashed #555;display:flex;flex-direction:column;align-items:center;justify-content:center;gap:14px}
.brand-mark{width:46px;height:46px;border-radius:50%;background:var(--teal)}
.brand-name{font-family:'Cinzel',serif;font-size:20px;color:#2b2420;letter-spacing:.5px}
.phone{right:65px;top:17px;display:flex;align-items:center;gap:6px;color:var(--teal);font-size:15px;letter-spacing:1px}
.nav{right:65px;top:54px;display:flex;align-items:center;font-size:14.5px;color:#6b6b6b}
.nav a{color:inherit;text-decoration:none;padding:0 15px;border-left:1px solid #ddd;line-height:14px}
.nav a:last-child{padding-right:0}
.nav .home{border:none;padding:0 14px 0 0}

/* hero */
.hero{left:0;top:96px;width:982px;height:398px;background:linear-gradient(160deg,#6a5a44 0%,#8c6a45 35%,#a87a4e 60%,#6b5138 100%)}
.hero-title{left:67px;top:250px;width:440px;font-family:'Cinzel',serif;font-weight:700;font-size:22px;line-height:30.5px;color:var(--white);letter-spacing:.3px;text-shadow:0 1px 3px rgba(0,0,0,.5)}
.dots{left:454px;top:472px;width:74px;height:22px;background:var(--white);border-radius:14px 14px 0 0;display:flex;justify-content:center;align-items:center;gap:6px;padding-top:2px}
.dots span{width:8px;height:8px;border:1px solid #555;border-radius:50%}
.dots span:last-child{background:#777}

/* seasons */
.season{top:546px;width:198px}
.season-head{display:flex;align-items:center;gap:9px;height:37px}
.season-icon{width:37px;height:37px;border-radius:50%;background:var(--ink);display:flex;align-items:center;justify-content:center}
.season-head h3{font-family:'Cinzel',serif;font-weight:400;font-size:17.5px;letter-spacing:1px;color:var(--ink);white-space:nowrap}
.season-photo{margin-top:7px;height:88px;border:1px solid #444;border-bottom:none}
.season-caption{position:relative;height:48px;background:var(--teal);color:var(--white);font-size:11.5px;line-height:15.2px;padding:2px 10px 0}
.season-caption.dark{background:var(--ink)}
.corner{position:absolute;right:0;bottom:0;width:28px;height:28px}

/* content sections */
.col{top:772px}
.col h2{font-family:'Cinzel',serif;font-weight:400;font-size:16.5px;letter-spacing:.6px;color:#333;padding-bottom:7px;border-bottom:1px solid var(--line);white-space:nowrap}
.about p{font-size:11.6px;line-height:17.5px;margin-top:13px;letter-spacing:.15px;text-align:justify}
.about p+p{margin-top:8px}
.benefits ul{list-style:none;margin-top:14px}
.benefits li{display:flex;gap:10px;font-size:10.2px;line-height:15.2px;margin-bottom:4px}
.benefits li svg{flex:none;margin-top:2px}
.btn{display:inline-block;background:var(--ink);color:var(--white);font-size:10px;font-weight:700;border-radius:3px;width:73px;height:22px;line-height:22px;text-align:center}
.field{height:27px;background:var(--field);border:1px solid #cfcfcf;border-radius:2px;font-size:10.5px;padding:7px 9px;margin-top:9px}
.field.first{margin-top:18px}
.field.msg{height:49px}

/* footer */
.footer{left:0;top:1062px;width:982px;height:102px;background:var(--teal-soft);color:var(--white)}
.foot-nav{left:0;top:17px;width:982px;display:flex;justify-content:center;font-size:12px;font-weight:700}
.foot-nav span.sep{margin:0 15px}
.foot-rule{left:228px;top:43px;width:526px;height:1px;background:rgba(255,255,255,.25)}
.contact{top:60px;display:flex;align-items:center;gap:8px;font-size:11px}
.contact-icon{width:29px;height:29px;border-radius:50%;background:var(--white);display:flex;align-items:center;justify-content:center}
.vrule{top:60px;width:1px;height:31px;background:rgba(255,255,255,.35)}
.follow{left:763px;top:68px;display:flex;align-items:center;gap:9px;font-size:13px;font-weight:700}
.follow i{width:12px;height:12px;border-radius:50%;background:var(--white);display:inline-block}
.copyright{left:0;top:1164px;width:982px;height:36px;background:var(--ink);color:#eee;font-size:10.5px;text-align:center;line-height:36px}
</style>
</head>
<body>
<div class="abs topbar"></div>

<header>
  <div class="abs brand"><div class="brand-inner"><div class="brand-mark"></div><div class="brand-name">MAPLE RIDGE</div></div></div>
  <div class="abs phone">
    <svg width="16" height="16" viewBox="0 0 24 24"><path fill="#2b2420" d="M6.6 10.8a15 15 0 0 0 6.6 6.6l2.2-2.2c.3-.3.7-.4 1-.2 1.1.4 2.3.6 3.6.6.6 0 1 .4 1 1V20c0 .6-.4 1-1 1A17 17 0 0 1 3 4c0-.6.4-1 1-1h3.5c.6 0 1 .4 1 1 0 1.3.2 2.5.6 3.6.1.3 0 .7-.2 1z"/></svg>
    555-014-2290
  </div>
  <nav class="abs nav">
    <a class="home" href="#"><svg width="22" height="18" viewBox="0 0 22 18"><path fill="#33b8a4" d="M11 0 0 9h3v9h6v-6h4v6h6V9h3z"/></svg></a>
    <a href="#">About Us</a><a href="#">Services</a><a href="#">Our Team</a><a href="#">Resources</a><a href="#">Contact Us</a>
  </nav>
</header>

<section class="abs hero" role="img" aria-label="Photo of a person raking a thick layer of autumn leaves in a wooded yard"></section>
<h1 class="abs hero-title">MAPLE RIDGE ARE A HOME UP KEEPING SERVICES AND MAINTENANCE FOR ALL SEASONS.</h1>
<div class="abs dots"><span></span><span></span><span></span><span></span></div>

<section>
  <article class="abs season" style="left:66px">
    <div class="season-head"><div class="season-icon"><svg width="20" height="20" viewBox="0 0 20 20" stroke="#fff" stroke-width="1.8" stroke-linecap="round"><path d="M10 1v18M2.2 5.5l15.6 9M2.2 14.5l15.6-9"/></svg></div><h3>Winter Season</h3></div>
    <div class="season-photo" role="img" aria-label="Photo of a cleared driveway between snow banks" style="background:linear-gradient(180deg,#c9a58c 0%,#d8d3cf 45%,#2e2f33 60%,#26272b 100%)"></div>
    <div class="season-caption">Lorem ipsum dolor sit amet, in the adipiscing magnagt Lorem ipsum dolor magnagt...
      <svg class="corner" viewBox="0 0 28 28"><path d="M28 0v28H0z" fill="#1b1b1b"/><path d="M19 14v9M14.5 18.5h9" stroke="#fff" stroke-width="2"/></svg></div>
  </article>
  <article class="abs season" style="left:284px">
    <div class="season-head"><div class="season-icon"><svg width="20" height="20" viewBox="0 0 20 20" fill="none" stroke="#fff" stroke-width="1.4"><path d="M10 2c4 3 5 7 0 12C5 9 6 5 10 2zM10 14v5"/></svg></div><h3>Fall Season</h3></div>
    <div class="season-photo" role="img" aria-label="Photo of a rake gathering red and orange leaves on grass" style="background:linear-gradient(160deg,#3f7a2a 0%,#8a3b1e 40%,#c9572a 65%,#7a2f1a 100%)"></div>
    <div class="season-caption dark">Lorem ipsum dolor sit amet, in the adipiscing magnagt Lorem ipsum dolor magnagt...
      <svg class="corner" viewBox="0 0 28 28"><path d="M28 0v28H0z" fill="#f78f20"/><path d="M19 14v9M14.5 18.5h9" stroke="#1b1b1b" stroke-width="2"/></svg></div>
  </article>
  <article class="abs season" style="left:498px">
    <div class="season-head"><div class="season-icon"><svg width="20" height="20" viewBox="0 0 20 20" fill="#fff"><circle cx="14" cy="5" r="2.2"/><path d="M2 17h16v1.5H2zM9 17c0-4 1-6 3-7-1 2-1 4-1 7z"/></svg></div><h3>Spring Season</h3></div>
    <div class="season-photo" role="img" aria-label="Photo of a gardener watering yellow flowers by a pond" style="background:linear-gradient(180deg,#6a8a3a 0%,#8ea53c 50%,#3f5b2c 100%)"></div>
    <div class="season-caption">Lorem ipsum dolor sit amet, in the adipiscing magnagt Lorem ipsum dolor magnagt...
      <svg class="corner" viewBox="0 0 28 28"><path d="M28 0v28H0z" fill="#1b1b1b"/><path d="M19 14v9M14.5 18.5h9" stroke="#fff" stroke-width="2"/></svg></div>
  </article>
  <article class="abs season" style="left:718px">
    <div class="season-head"><div class="season-icon"><svg width="22" height="22" viewBox="0 0 22 22" fill="none" stroke="#fff" stroke-width="1.6"><circle cx="11" cy="11" r="4.5"/><circle cx="11" cy="11" r="8"/></svg></div><h3>Summer Season</h3></div>
    <div class="season-photo" role="img" aria-label="Photo of a lawn mower cutting a green lawn" style="background:linear-gradient(120deg,#4a5a3a 0%,#6f9a38 45%,#8fbf4a 100%)"></div>
    <div class="season-caption">Lorem ipsum dolor sit amet, in the adipiscing magnagt Lorem ipsum dolor magnagt...
      <svg class="corner" viewBox="0 0 28 28"><path d="M28 0v28H0z" fill="#1b1b1b"/><path d="M19 14v9M14.5 18.5h9" stroke="#fff" stroke-width="2"/></svg></div>
  </article>
</section>

<section class="abs col about" style="left:68px;width:259px">
  <h2>About Us</h2>
  <p>Lorem ipsum dolor sit amet, consectetuer adipiscing elit, sed diam nonummy nibh euismod tincidunt ut laoreet dolore magna aliquam erat volutpat. Ut wisi enim ad minim veniam.</p>
  <p>Lorem ipsum dolor sit amet, consectetuer adipiscing elit, sed diam nonummy nibh euismod tincidunt ut laoreet dolore magna aliquam erat volutpat. Ut wisi enim ad minim veniam, quis nostrud exea commodo consequat.</p>
</section>
<a class="abs btn" style="left:68px;top:998px">Read More</a>

<section class="abs col benefits" style="left:360px;width:260px">
  <h2>Banefits to Our Customers</h2>
  <ul>
    <li><svg width="13" height="11" viewBox="0 0 13 11"><path d="M1 6l3.5 3.5L12 1" fill="none" stroke="#1b1b1b" stroke-width="2.2"/></svg><span>Extra time to far too often very busy / demanding lives.</span></li>
    <li><svg width="13" height="11" viewBox="0 0 13 11"><path d="M1 6l3.5 3.5L12 1" fill="none" stroke="#1b1b1b" stroke-width="2.2"/></svg><span>Saving by performing ongoing maintenance and fixing-before-failure which lowers the Total Cost of Home Ownership.</span></li>
    <li><svg width="13" height="11" viewBox="0 0 13 11"><path d="M1 6l3.5 3.5L12 1" fill="none" stroke="#1b1b1b" stroke-width="2.2"/></svg><span>Less work and things to do around the house.</span></li>
    <li><svg width="13" height="11" viewBox="0 0 13 11"><path d="M1 6l3.5 3.5L12 1" fill="none" stroke="#1b1b1b" stroke-width="2.2"/></svg><span>Stress reduction with many fewer items on 'To-do' lists and additional time to spend on whatever fun/relaxing activities our customers desire.</span></li>
  </ul>
</section>
<a class="abs btn" style="left:382px;top:998px">Read More</a>

<section class="abs col inquiry" style="left:655px;width:261px">
  <h2>Quick Inquiry</h2>
  <div class="field first">Name :</div>
  <div class="field">Email :</div>
  <div class="field">Phone :</div>
  <div class="field msg">Message :</div>
</section>
<a class="abs btn" style="left:655px;top:998px">Send</a>

<footer>
  <div class="abs footer">
    <div class="abs foot-nav"><span>Home</span><span class="sep">•</span><span>About Us</span><span class="sep">•</span><span>Services</span><span class="sep">•</span><span>Our Team</span><span class="sep">•</span><span>Resources</span><span class="sep">•</span><span>Contact Us</span></div>
    <div class="abs foot-rule"></div>
    <div class="abs contact" style="left:66px"><div class="contact-icon"><svg width="12" height="16" viewBox="0 0 12 16"><path d="M6 0a6 6 0 0 0-6 6c0 4.5 6 10 6 10s6-5.5 6-10a6 6 0 0 0-6-6zm0 8.2A2.2 2.2 0 1 1 6 3.8a2.2 2.2 0 0 1 0 4.4z" fill="#1b1b1b"/></svg></div><div><b>Maple Ridge</b><br>Lorem ipsum dolor sit amet.</div></div>
    <div class="abs vrule" style="left:276px"></div>
    <div class="abs contact" style="left:315px"><div class="contact-icon"><svg width="14" height="14" viewBox="0 0 24 24"><path fill="#1b1b1b" d="M6.6 10.8a15 15 0 0 0 6.6 6.6l2.2-2.2c.3-.3.7-.4 1-.2 1.1.4 2.3.6 3.6.6.6 0 1 .4 1 1V20c0 .6-.4 1-1 1A17 17 0 0 1 3 4c0-.6.4-1 1-1h3.5c.6 0 1 .4 1 1 0 1.3.2 2.5.6 3.6.1.3 0 .7-.2 1z"/></svg></div>555.014.7731</div>
    <div class="abs vrule" style="left:492px"></div>
    <div class="abs contact" style="left:532px"><div class="contact-icon"><svg width="15" height="11" viewBox="0 0 15 11"><rect width="15" height="11" rx="1.5" fill="#1b1b1b"/><path d="M1 1.5l6.5 5 6.5-5" fill="none" stroke="#fff" stroke-width="1.2"/></svg></div>hello@mapleridgeyards.com</div>
    <div class="abs vrule" style="left:722px"></div>
    <div class="abs follow">Follow Us <i></i><i></i><i></i><i></i></div>
  </div>
  <div class="abs copyright">Copyright © 2016 MAPLE RIDGE. All Rights Reserved.</div>
</footer>
</body>
</html>
```